Christmas social media advert post

I am looking for an eye catching advert for use mainly on social media posts.
The following is the detail of the event.

Christmas special offer-
£10pp,– offer includes –
Half an hour Toboggan track,
Half an hour Slingshot paintballs (20 paintballs pp) and safe target archery (under cover and indoor ranges). Activities all the family from age 4 to grandparents can join in,
Also available – Add on indoor activities including Mini Curling, Bead Blitz, Safe axe throwing, Air juggler – from £3.50pp and age 6plus
Café open for hot food and drinks in the ‘Fireside Frost Lodge and the heated Christmas marquee.

A basic idea I put together for what I feel is the important information is -

Christmas Special offer -
Starts Saturday 20th December.
£10pp – offer includes –
Half an hour Slingshot paintballs (20 paintballs pp) and safe target archery (under cover and indoor ranges). Activities all the family from age 4 to grandparents can join in. Booking is essential - details on how below.
Also available Add on indoor activities - including Mini Curling, Bead Blitz, Safe axe throwing, Air juggler – from £3.50pp and age 6plus.
Ages start from 4 plus.
All activities are great for children and adults so perfect for families as well as friends, parties and get togethers.
Free huge car parks,
Booking is easy-
Just Message from messenger (on this post) or email
martin@hollowbrookleisurepark.co.uk for availability of your preferred date and time.

I would be happy to send the detailed information to enquiries if it meant a better looking advert / post.

Full details are in the picture uploads, feel free to use as much or as little of the information as you feel best.

```html
<!DOCTYPE html>
<html lang="en">
<head>
<meta charset="utf-8">
<title>Christmas Special Offer – Social Posts</title>
<link href="https://fonts.googleapis.com/css2?family=Oswald:wght@400;500;600;700&family=Montserrat:ital,wght@0,600;0,700;1,600;1,800;1,900&display=swap" rel="stylesheet">
<style>
  :root{
    --stage:#000000;
    --red:#ff1010;
    --green:#13c13a;
    --yellow:#ffe600;
    --white:#ffffff;
    --ink:#111111;
    --brand-blue:#1f3fa8;
    --snow-top:#f4f6fa;
    --snow-bottom:#dde3ec;
  }
  *{margin:0;padding:0;box-sizing:border-box}
  html,body{width:1200px;height:600px;overflow:hidden;background:var(--stage)}
  .stage{position:relative;width:1200px;height:600px}
  .post{position:absolute;top:170px;width:260px;height:260px;overflow:hidden;font-family:'Oswald',sans-serif;color:var(--white)}
  .post--intro{left:38px}
  .post--offer{left:324px}
  .post--addons{left:610px;background:var(--green)}
  .post--booking{left:902px}
  .snow-bg{position:absolute;inset:0;background:linear-gradient(180deg,var(--snow-top) 0%,#ffffff 45%,var(--snow-bottom) 100%)}
  .abs{position:absolute;white-space:nowrap}
  .placeholder{position:absolute}
  .next-arrows{position:absolute;width:30px;height:18px}

  /* intro */
  .intro-red{left:55px;top:0;width:149px;height:175px;background:var(--red)}
  .intro-green{left:55px;top:175px;width:149px;height:66px;background:var(--green)}
  .bells{left:95px;top:7px;width:70px;height:56px;border-radius:40%;background:radial-gradient(circle,#f4d23a 0%,#d8a41a 60%,#2fa84a 100%)}
  .snowman{left:199px;top:130px;width:52px;height:84px;border-radius:45%;background:radial-gradient(circle at 50% 65%,#ffffff 0%,#e8ecf2 70%,#c9d2de 100%)}
  .holly{left:14px;top:166px;width:40px;height:32px;border-radius:50%;background:radial-gradient(circle,#d2202a 0%,#3c8b2e 60%,transparent 75%)}
  .headline{position:absolute;left:55px;width:149px;text-align:center;font-weight:700;line-height:1;letter-spacing:-0.5px}
  .h-christmas{top:61px;font-size:29px}
  .h-special{top:87px;font-size:37px}
  .h-offer{top:120px;font-size:49px}
  .starts{left:62px;top:180px;font-size:13px;font-weight:500;line-height:16px}
  .saturday{left:103px;top:177px;font-size:22px;font-weight:600;line-height:28px;letter-spacing:-0.3px}
  .date-rule{left:103px;top:209px;width:94px;height:1px;background:var(--white)}
  .day{left:61px;top:196px;font-size:38px;font-weight:600;line-height:44px}
  .suffix{left:100px;top:216px;font-size:13px;font-weight:600;line-height:16px}
  .month{left:116px;top:212px;font-size:19px;font-weight:600;line-height:24px}

  /* offer */
  .photo-toboggan{left:0;top:0;width:164px;height:86px;background:linear-gradient(135deg,#b9a48a,#8d7f72 60%,#c43a30)}
  .photo-slingshot{left:0;top:87px;width:164px;height:86px;background:linear-gradient(135deg,#3b3f34,#6b3f6a 55%,#2a2b30)}
  .photo-archery{left:0;top:174px;width:164px;height:86px;background:linear-gradient(135deg,#6e6a63,#a9a49a 55%,#3a3835)}
  .offer-panel{left:164px;top:0;width:96px;height:260px;background:var(--red)}
  .offer-copy{position:absolute;left:164px;width:96px;text-align:center;white-space:nowrap}
  .price{top:2px;color:var(--yellow);font-weight:700;font-size:34px;line-height:40px}
  .price small{font-size:15px}
  .includes{top:41px;font-family:'Montserrat',sans-serif;font-weight:600;font-size:9px;line-height:10px}
  .half{font-family:'Montserrat',sans-serif;font-weight:700;font-size:8px;line-height:10px;color:var(--yellow)}
  .half-1{top:68px}
  .half-2{top:121px}
  .activity{font-weight:500;font-size:17px;line-height:19px;letter-spacing:-0.2px}
  .act-toboggan{top:78px}
  .act-sling{top:131px}
  .note{font-family:'Montserrat',sans-serif;font-style:italic;font-weight:600;font-size:7.5px;line-height:10px;color:var(--yellow)}
  .note-balls{top:171px}
  .act-archery{top:185px;font-size:16px;line-height:18px}
  .note-ranges{top:222px}

  /* addons */
  .addons-photo{left:0;top:23px;width:260px;height:237px;background:linear-gradient(120deg,#c9b79b 0%,#e2d6c4 40%,#b39a7a 70%,#2a4fb0 85%,#c8262a 100%)}
  .also{left:52px;top:15px;width:156px;height:23px;background:var(--red);text-align:center;font-family:'Montserrat',sans-serif;font-weight:700;font-size:14px;letter-spacing:1px;line-height:23px}
  .addon-head{left:174px;top:40px;width:86px;height:73px;background:var(--green)}
  .addon-line{position:absolute;left:182px;font-weight:500;line-height:1;white-space:nowrap}
  .al-1{top:44px;font-size:18px}
  .al-2{top:63px;font-size:23px}
  .al-3{top:87px;font-size:16px}
  .addon-list{left:0;top:156px;width:140px;height:104px;background:var(--green)}
  .addon-item{position:absolute;left:11px;font-weight:500;font-size:11.5px;line-height:14px;white-space:nowrap;letter-spacing:-0.1px}
  .ai-1{top:161px}
  .ai-2{top:182px}
  .ai-3{top:202px}
  .ai-4{top:223px}
  .addon-rule{position:absolute;left:11px;height:1px;background:var(--white)}
  .ar-1{top:177px;width:110px}
  .ar-2{top:198px;width:100px}
  .ar-3{top:218px;width:100px}
  .addon-price{position:absolute;left:11px;top:240px;font-weight:500;font-size:9px;line-height:12px;color:var(--yellow);white-space:nowrap}
  .gingerbread{left:122px;top:102px;width:36px;height:52px;border-radius:40%;background:radial-gradient(circle,#e7a24a,#b8702a)}

  /* booking */
  .book-green{left:18px;top:18px;width:224px;height:89px;background:var(--green)}
  .book-title{left:18px;top:25px;width:224px;text-align:center;font-family:'Montserrat',sans-serif;font-style:italic;font-weight:900;font-size:17px}
  .book-dm{left:18px;top:49px;width:224px;text-align:center;font-family:'Montserrat',sans-serif;font-weight:600;font-size:7.5px}
  .email-box{left:26px;top:63px;width:208px;height:15px;border:1.5px solid var(--ink);border-radius:4px;color:var(--ink);text-align:center;font-size:9.5px;line-height:12px;font-weight:500}
  .book-note{left:18px;top:81px;width:206px;text-align:center;font-family:'Montserrat',sans-serif;font-style:italic;font-weight:600;font-size:7.5px}
  .cursor{left:214px;top:78px;width:15px;height:16px}
  .parks{left:33px;top:96px;width:194px;height:28px;background:var(--red);text-align:center;font-family:'Montserrat',sans-serif;font-style:italic;font-weight:800;font-size:15px;line-height:28px}
  .brand{left:65px;top:138px;display:flex;align-items:center;gap:8px;color:var(--brand-blue)}
  .brand-dot{width:52px;height:52px;border-radius:50%;background:var(--brand-blue)}
  .brand-name{font-weight:700;font-size:15px;line-height:1.05;text-transform:uppercase}
  .ages{left:18px;top:201px;width:224px;height:44px;background:var(--red);text-align:center}
  .ages-head{font-weight:500;font-size:18px;line-height:1.2;padding-top:3px}
  .ages-sub{font-size:6.5px;font-weight:500;line-height:1.2}
</style>
</head>
<body>
<main class="stage">

  <section class="post post--intro">
    <div class="snow-bg"></div>
    <div class="abs intro-red"></div>
    <div class="abs intro-green"></div>
    <div class="placeholder snowman" role="img" aria-label="Cartoon snowman with top hat and scarf"></div>
    <div class="placeholder holly" role="img" aria-label="Holly leaves and berries"></div>
    <div class="placeholder bells" role="img" aria-label="Golden Christmas bells with a green bow"></div>
    <div class="headline h-christmas">CHRISTMAS</div>
    <div class="headline h-special">SPECIAL</div>
    <div class="headline h-offer">OFFER</div>
    <div class="abs starts">STARTS</div>
    <div class="abs saturday">SATURDAY</div>
    <div class="abs date-rule"></div>
    <div class="abs day">20</div>
    <div class="abs suffix">TH</div>
    <div class="abs month">DECEMBER</div>
    <svg class="next-arrows" style="left:224px;top:232px" viewBox="0 0 30 18"><path d="M0 0L10 9L0 18Z" fill="var(--green)"/><path d="M10 0L20 9L10 18Z" fill="var(--green)"/><path d="M20 0L30 9L20 18Z" fill="var(--red)"/></svg>
  </section>

  <section class="post post--offer">
    <div class="placeholder photo-toboggan" role="img" aria-label="Photo of children in helmets riding the toboggan track"></div>
    <div class="placeholder photo-slingshot" role="img" aria-label="Photo of players aiming slingshots in the lit paintball range"></div>
    <div class="placeholder photo-archery" role="img" aria-label="Photo of archers shooting at targets on the covered range"></div>
    <div class="abs offer-panel"></div>
    <div class="offer-copy price">£10<small>PP</small></div>
    <div class="offer-copy includes">OFFER<br>INCLUDES:</div>
    <div class="offer-copy half half-1">Half An Hour</div>
    <div class="offer-copy activity act-toboggan">TOBOGGAN<br>TRACK</div>
    <div class="offer-copy half half-2">Half An Hour</div>
    <div class="offer-copy activity act-sling">SLINGSHOT<br>PAINTBALLS</div>
    <div class="offer-copy note note-balls">(20 Paintballs PP)</div>
    <div class="offer-copy activity act-archery">SAFE TARGET<br>ARCHERY</div>
    <div class="offer-copy note note-ranges">(under Cover And<br>Indoor Ranges)</div>
    <svg class="next-arrows" style="left:14px;top:232px" viewBox="0 0 30 18"><path d="M0 0L10 9L0 18Z" fill="var(--green)"/><path d="M10 0L20 9L10 18Z" fill="var(--red)"/><path d="M20 0L30 9L20 18Z" fill="var(--red)"/></svg>
  </section>

  <section class="post post--addons">
    <div class="placeholder addons-photo" role="img" aria-label="Photo of people playing mini curling indoors beside an axe throwing target"></div>
    <div class="abs also">ALSO AVAILABLE</div>
    <div class="abs addon-head"></div>
    <div class="addon-line al-1">ADD ON</div>
    <div class="addon-line al-2">INDOOR</div>
    <div class="addon-line al-3">ACTIVITIES</div>
    <div class="placeholder gingerbread" role="img" aria-label="Gingerbread man decoration"></div>
    <div class="abs addon-list"></div>
    <div class="addon-item ai-1">INCLUDING MINI CURLING</div>
    <div class="addon-rule ar-1"></div>
    <div class="addon-item ai-2">BEAD BLITZ</div>
    <div class="addon-rule ar-2"></div>
    <div class="addon-item ai-3">SAFE AXE THROWING</div>
    <div class="addon-rule ar-3"></div>
    <div class="addon-item ai-4">AIR JUGGLER</div>
    <div class="addon-price">FROM £3.50PP AND AGE 6 PLUS</div>
    <svg class="next-arrows" style="left:218px;top:232px" viewBox="0 0 30 18"><path d="M0 0L10 9L0 18Z" fill="var(--red)"/><path d="M10 0L20 9L10 18Z" fill="var(--red)"/><path d="M20 0L30 9L20 18Z" fill="var(--red)"/></svg>
  </section>

  <section class="post post--booking">
    <div class="snow-bg"></div>
    <div class="abs book-green"></div>
    <div class="abs book-title">BOOKING IS EASY!</div>
    <div class="abs book-dm">DM ON THIS POST OR EMAIL :</div>
    <div class="abs email-box">martin@hollowbrookleisurepark.co.uk</div>
    <div class="abs book-note">for availability of your preferred date and time</div>
    <svg class="abs cursor" viewBox="0 0 15 16"><path d="M1 1L1 12L4 9.5L6.5 15L9 14L6.5 8.5L11 8.5Z" fill="var(--white)" stroke="var(--ink)" stroke-width="1.2" stroke-linejoin="round"/></svg>
    <div class="abs parks">FREE HUGE CAR PARKS</div>
    <div class="abs brand">
      <div class="brand-dot"></div>
      <div class="brand-name">Hollowbrook<br>Leisure Park</div>
    </div>
    <div class="abs ages">
      <div class="ages-head">AGES START FROM 4 PLUS</div>
      <div class="ages-sub">ALL ACTIVITIES ARE GREAT FOR CHILDREN AND ADULTS<br>SO PERFECT FOR FAMILIES AS WELL AS FRIENDS, PARTIES AND GET TOGETHERS.</div>
    </div>
  </section>

</main>
</body>
</html>
```